Sleek and Morden Business Card

Business Card Design for Business Name "Lantern Pine Services (LPS)"
Offering Virtual Assistant (VA) services including Virtual Receptionist, Appointment and Diary Management. Taking and Answering calls for Sole Trader Businesses. Quotes, Invoices, Expense Reconciliation, Accounts Payable and Accounts Receivable.
Lantern Services offers clients the ease of a complete office without the physical need to having an office.
Target Market(s)
Target market are Sole Traders like Electricians, Plumbers, Painters etc.
Industry/Entity Type
Business
Colors
Designer to choose colors to be used in the design.
Look and feel
Each slider illustrates characteristics of the customer's brand and the style your logo design should communicate.

```html
<!DOCTYPE html>
<html lang="en">
<head>
<meta charset="utf-8">
<title>Lantern Pine Services – Business Card</title>
<link rel="stylesheet" href="https://fonts.googleapis.com/css2?family=Open+Sans:wght@400;600;700;800&display=swap">
<style>
  :root {
    --brand-blue: #0b6aa8;
    --brand-blue-deep: #07548c;
    --brand-blue-light: #0a9ad8;
    --ink-grey: #555a60;
    --soft-grey: #8a8f95;
    --divider: #d6d9dd;
    --paper: #ffffff;
    --stage: #1c1c1c;
  }
  * { box-sizing: border-box; margin: 0; padding: 0; }
  html, body { width: 798px; height: 1200px; overflow: hidden; }
  body {
    font-family: "Open Sans", Arial, sans-serif;
    background: var(--paper);
    position: relative;
  }

  /* Identity block */
  .identity {
    position: absolute; top: 0; left: 0;
    width: 798px; height: 384px;
    display: flex; flex-direction: column; align-items: center;
    padding-top: 92px;
    background: var(--paper);
  }
  .identity__mark {
    font-weight: 800; font-size: 112px; line-height: 1;
    letter-spacing: 2px; color: var(--brand-blue);
  }
  .identity__name {
    margin-top: 10px;
    font-size: 17px; letter-spacing: 1.5px; color: var(--ink-grey);
  }
  .identity__tagline {
    margin-top: 8px;
    font-size: 9.5px; line-height: 16px; text-align: center; color: var(--soft-grey);
  }

  /* Card display area */
  .cards {
    position: absolute; top: 384px; left: 0;
    width: 798px; height: 816px;
    background: var(--stage);
    display: flex; flex-direction: column; align-items: center;
    justify-content: center; gap: 44px;
  }
  .card {
    width: 560px; height: 310px; position: relative; overflow: hidden;
  }

  /* Front */
  .card--front { background: var(--paper); }
  .card__brand {
    position: absolute; left: 34px; top: 72px; width: 200px; text-align: center;
  }
  .card__brand-mark {
    font-weight: 800; font-size: 64px; line-height: 1; color: var(--brand-blue);
  }
  .card__brand-name {
    margin-top: 6px; font-size: 12px; color: var(--ink-grey);
  }
  .card__divider {
    position: absolute; left: 238px; top: 50px; width: 1px; height: 150px;
    background: linear-gradient(to bottom, transparent, var(--divider) 20%, var(--divider) 80%, transparent);
  }
  .card__contact { position: absolute; left: 270px; top: 66px; }
  .card__person { font-weight: 700; font-size: 17px; color: var(--brand-blue-deep); }
  .card__role { font-size: 13px; color: var(--ink-grey); letter-spacing: .5px; }
  .card__details {
    margin-top: 18px; font-size: 13.5px; line-height: 24px; color: var(--ink-grey);
    letter-spacing: .5px;
  }
  .card__details dt { display: inline-block; width: 66px; }
  .card__details dd { display: inline; }
  .card__services {
    position: absolute; left: 0; right: 0; bottom: 16px;
    font-size: 9px; line-height: 15px; text-align: center; color: var(--soft-grey);
  }

  /* Back */
  .card--back {
    background: linear-gradient(135deg, var(--brand-blue-light) 0%, var(--brand-blue) 55%, var(--brand-blue-deep) 100%);
    display: flex; flex-direction: column; align-items: center; justify-content: center;
  }
  .card__back-mark {
    font-weight: 800; font-size: 88px; line-height: 1; color: var(--paper); letter-spacing: 2px;
  }
  .card__back-name {
    margin-top: 4px; font-size: 15px; color: var(--paper); letter-spacing: .8px;
  }
</style>
</head>
<body>

<header class="identity">
  <div class="identity__mark">LPS</div>
  <div class="identity__name">Lantern Pine Services</div>
  <p class="identity__tagline">
    Get the help you need, when you need it!<br>
    Virtual Assistant (VA) services include Remote Receptionist | Appointment Bookings |<br>
    Calendar and Diary Management | Job Management - Quotes and Invoices |<br>
    Expense Reconciliation | Accounts Payable | Accounts Receivable
  </p>
</header>

<main class="cards">
  <section class="card card--front" aria-label="Card front">
    <div class="card__brand">
      <div class="card__brand-mark">LPS</div>
      <div class="card__brand-name">Lantern Pine Services</div>
    </div>
    <div class="card__divider"></div>
    <div class="card__contact">
      <div class="card__person">Mara Quillon</div>
      <div class="card__role">Director</div>
      <dl class="card__details">
        <div><dt>Mobile:</dt><dd>0400 555 182</dd></div>
        <div><dt>Email &nbsp;:</dt><dd>mara@lanternpine.com.au</dd></div>
      </dl>
    </div>
    <p class="card__services">
      Get the help you need, when you need it!<br>
      Virtual Assistant (VA) services include Remote Receptionist | Appointment Bookings |<br>
      Calendar and Diary Management | Job Management - Quotes and Invoices |<br>
      Expense Reconciliation | Accounts Payable | Accounts Receivable
    </p>
  </section>

  <section class="card card--back" aria-label="Card back">
    <div class="card__back-mark">LPS</div>
    <div class="card__back-name">Lantern Pine Services</div>
  </section>
</main>

</body>
</html>
```